vantrel works cybersecurity website design and development

website design and development for a cybersecurity company. we have a logo and would like site to suit logo colors and look
cybersecurity website should be secure and look professional
main example of site we want to use: https://www.morvisquad.example/
site should be usable on tablet and phones

For each design proposal, please could you provide details of what language you'll use to code the website.

Target Market(s)

insurance companies, financial institutions, private SME, Africa and Europe

Coding

Coded - Design and coding required

Number of Pages Required

5+ page

Requirements
Must have
• 9 Pages:
Home
About us
Contacts
Partners
Blog
Services
( consulting, vulnerability assessment, information systems security audit, ISO compliance, Penetration testing, security awareness training, social engineering test, protection against DDoS, procurement )
Resources
Technologies
Careers
Nice to have
• nice to have all services have their own pages.
design based on logo colors and look

please provide what will be use to code the website

```html
<!DOCTYPE html>
<html lang="en">
<head>
<meta charset="utf-8">
<title>Vantrel Works – Cybersecure Your Business</title>
<link rel="stylesheet" href="https://fonts.googleapis.com/css2?family=Lato:wght@400;700;900&display=swap">
<style>
:root{
  --navy:#0b1450;
  --deep:#1a237e;
  --mid:#0d4fa3;
  --bright:#1382d6;
  --nav:#0f6cc4;
  --grey:#f1f1f1;
  --text:#333;
  --muted:#555;
  --footer:#1b1b1b;
  --white:#fff;
}
*{margin:0;padding:0;box-sizing:border-box}
html,body{width:1200px;height:4736px;overflow:hidden}
body{font-family:"Lato",sans-serif;color:var(--text);background:var(--white);position:relative}
.abs{position:absolute}
.ph{position:absolute}
/* header */
.brand{left:75px;top:24px;display:flex;align-items:center;gap:12px}
.brand-mark{width:70px;height:70px;border-radius:50%;background:var(--mid)}
.brand-name{font-weight:900;font-size:32px;color:var(--mid);line-height:1}
.brand-tag{font-size:9px;font-weight:700;color:var(--mid);letter-spacing:.5px;margin-top:3px}
.top-contact{right:75px;top:52px;font-size:16px;color:#444;display:flex;gap:18px;align-items:center}
.nav{top:117px;left:0;width:1200px;height:51px;background:var(--nav);display:flex;justify-content:center;gap:42px;align-items:center}
.nav a{color:#fff;font-size:13px;font-weight:700;text-decoration:none}
/* hero */
.hero-title{left:75px;top:350px;font-size:90px;font-weight:900;color:#fff;line-height:1}
.hero-sub{left:77px;top:448px;font-size:30px;font-weight:700;color:#fff}
.btn{display:flex;align-items:center;justify-content:center;border-radius:24px;font-weight:700;color:#fff;font-size:16px}
.btn-solid{background:var(--deep);border:2px solid #2b5bd0}
.btn-line{border:2px solid #fff;font-size:15px}
/* partners */
.section-h{width:1200px;left:0;text-align:center;font-weight:700}
.partners{top:1020px;left:110px;width:980px;height:152px;display:flex}
.partner{flex:1;display:flex;align-items:center;justify-content:center;gap:10px;font-weight:700;font-size:24px;color:var(--mid);border-right:1px solid #ddd}
.partner:last-child{border-right:none}
.arrow{font-size:40px;color:#555;font-weight:700}
/* services */
.card{top:1581px;width:330px;height:357px;color:#fff;text-align:center;padding-top:36px}
.card h3{font-size:18px;font-weight:900;margin-top:16px}
.card p{font-size:14px;line-height:26px;margin:12px auto 0;width:270px}
.card .btn{width:178px;height:44px;margin:26px auto 0}
/* about */
.about-h{left:571px;top:2138px;font-size:34px;font-weight:700;color:#222}
.about-p{left:571px;top:2188px;width:545px;font-size:14px;line-height:28px;color:var(--muted)}
/* testimonials */
.testi-p{left:170px;top:2640px;width:860px;text-align:center;color:#fff;font-size:15.5px;line-height:31px}
.avatar{border-radius:50%;border:4px solid #fff;background:linear-gradient(#8a9bb0,#3a4a60)}
/* blog */
.post{top:3110px;width:330px;text-align:center}
.post-img{height:218px;position:relative}
.post-date{position:absolute;bottom:0;left:30px;right:30px;height:34px;background:#fff;color:var(--deep);font-size:13px;font-weight:700;display:flex;align-items:center;justify-content:center}
.post h4{font-size:18px;font-weight:700;color:#222;margin-top:12px;line-height:27px}
.post p{font-size:14px;color:var(--muted);line-height:26px;margin-top:8px;padding:0 14px}
/* contact */
.field{background:#fff;height:45px;font-size:13px;font-weight:700;color:#333;padding:12px 14px}
/* footer */
.foot-h{font-size:20px;font-weight:700;color:#fff}
.foot-list{list-style:none;font-size:14px;color:#ddd;line-height:31px;margin-top:8px}
.foot-icon{width:42px;height:42px;border-radius:50%;border:2px solid #fff;display:flex;align-items:center;justify-content:center}
.social{display:flex;gap:12px;font-size:12px;font-weight:700;color:#fff}
.copy{top:4680px;left:0;width:1200px;height:56px;background:var(--nav);color:#fff;font-size:12px;display:flex;align-items:center;justify-content:center}
</style>
</head>
<body>

<!-- header -->
<div class="abs brand">
  <div class="brand-mark"></div>
  <div><div class="brand-name">Vantrel Works</div><div class="brand-tag">CYBERSECURE YOUR BUSINESS</div></div>
</div>
<div class="abs top-contact">
  <span><svg width="14" height="14" viewBox="0 0 24 24"><path fill="#444" d="M6.6 10.8a15 15 0 006.6 6.6l2.2-2.2c.3-.3.7-.4 1-.2 1.1.4 2.3.6 3.6.6.6 0 1 .4 1 1V20c0 .6-.4 1-1 1A17 17 0 013 4c0-.6.4-1 1-1h3.5c.6 0 1 .4 1 1 0 1.3.2 2.5.6 3.6.1.3 0 .7-.2 1z"/></svg> 1-800-555-0142</span>
  <span>|</span>
  <span><svg width="15" height="12" viewBox="0 0 24 18"><rect width="24" height="18" rx="2" fill="#444"/><path d="M1 2l11 8 11-8" stroke="#fff" stroke-width="2" fill="none"/></svg> info@vantrelworks.example</span>
</div>
<nav class="abs nav">
  <a>HOME</a><a>WHO WE ARE</a><a>WHAT WE DO</a><a>CLIENTS</a><a>OUR WORK</a><a>BLOG</a><a>CONTACT</a>
</nav>

<!-- hero -->
<svg class="abs" style="top:168px;left:0" width="1200" height="720" viewBox="0 0 1200 720">
  <defs>
    <radialGradient id="heroBg" cx="0.35" cy="0.75" r="0.9">
      <stop offset="0" stop-color="#163a7a"/><stop offset=".5" stop-color="#0a1a45"/><stop offset="1" stop-color="#03091f"/>
    </radialGradient>
  </defs>
  <rect width="1200" height="720" fill="url(#heroBg)" role="img" aria-label="Dark blue digital network background"/>
  <path d="M0 610 C150 560 230 520 330 545 C430 570 430 650 560 690 C700 730 790 680 900 640 C1000 605 1100 630 1200 650 L1200 720 L0 720Z" fill="#fff"/>
</svg>
<div class="ph" role="img" aria-label="Green chameleon perched on a brass padlock" style="left:660px;top:250px;width:540px;height:560px;background:radial-gradient(ellipse at 55% 60%,#b07a30 0%,#6e8a3a 35%,rgba(20,40,30,0) 70%)"></div>
<div class="abs hero-title">Vantrel Works</div>
<div class="abs hero-sub">Cybersecure Your Business</div>
<div class="abs btn btn-solid" style="left:77px;top:518px;width:176px;height:42px">Read More</div>

<!-- partners -->
<div class="abs section-h" style="top:948px;font-size:23px;color:#333;font-weight:400">They already trusted us</div>
<div class="abs arrow" style="left:40px;top:1072px">‹</div>
<div class="abs partners">
  <div class="partner"><span style="width:22px;height:22px;border-radius:50%;background:var(--mid)"></span>Brandell</div>
  <div class="partner">Orvane</div>
  <div class="partner">Quastor</div>
  <div class="partner">Nexaro</div>
</div>
<div class="abs arrow" style="left:1138px;top:1072px">›</div>

<!-- services -->
<svg class="abs" style="top:1200px;left:0" width="1200" height="830" viewBox="0 0 1200 830">
  <path d="M0 110 C120 60 260 40 390 80 C520 120 540 70 640 80 C760 95 780 240 900 225 C1020 210 1100 145 1200 165 L1200 830 L0 830Z" fill="var(--grey)"/>
</svg>
<div class="ph" role="img" aria-label="Colourful chameleon on a branch" style="left:0;top:1205px;width:370px;height:230px;background:radial-gradient(ellipse at 50% 45%,#e8a030 0%,#3aa0a0 40%,rgba(255,255,255,0) 72%)"></div>
<div class="abs section-h" style="top:1503px;font-size:32px;color:#222">OUR SERVICES</div>

<div class="abs card" style="left:75px;background:var(--deep)">
  <svg width="70" height="64" viewBox="0 0 70 64"><circle cx="26" cy="34" r="16" fill="none" stroke="#fff" stroke-width="9" stroke-dasharray="6 4"/><circle cx="26" cy="34" r="6" fill="#fff"/><circle cx="54" cy="16" r="9" fill="none" stroke="#fff" stroke-width="6" stroke-dasharray="4 3"/><circle cx="54" cy="48" r="8" fill="none" stroke="#fff" stroke-width="6" stroke-dasharray="4 3"/></svg>
  <h3>SECURITY ASSESSMENT</h3>
  <p>Sed ut perspiciatis unde omnis iste natus error sit voluptatem accusantium doloremque architecto beatae vitae dicta magni.</p>
  <div class="btn btn-line">Learn More</div>
</div>
<div class="abs card" style="left:436px;background:var(--mid)">
  <svg width="64" height="64" viewBox="0 0 64 64"><path d="M32 4 L56 12 V30 C56 46 45 56 32 60 C19 56 8 46 8 30 V12Z" fill="#fff"/><path d="M32 12 L48 17 V30 C48 42 41 49 32 52Z" fill="var(--mid)"/></svg>
  <h3>SECURITY ENHANCEMENT</h3>
  <p>Sed ut perspiciatis unde omnis iste natus error sit voluptatem accusantium doloremque architecto beatae vitae dicta magni.</p>
  <div class="btn btn-line">Learn More</div>
</div>
<div class="abs card" style="left:796px;background:var(--bright)">
  <svg width="64" height="64" viewBox="0 0 64 64"><path d="M12 28 A20 20 0 0 1 48 18" fill="none" stroke="#fff" stroke-width="8"/><path d="M52 6 V26 H32Z" fill="#fff"/><path d="M52 36 A20 20 0 0 1 16 46" fill="none" stroke="#fff" stroke-width="8"/><path d="M12 58 V38 H32Z" fill="#fff"/></svg>
  <h3>RISK COMPLIANCE</h3>
  <p>Sed ut perspiciatis unde omnis iste natus error sit voluptatem accusantium doloremque architecto beatae vitae dicta magni.</p>
  <div class="btn btn-line">Learn More</div>
</div>

<!-- about -->
<div class="abs" style="left:75px;top:2110px;width:468px;height:338px;background:var(--deep);clip-path:polygon(0 0,4% 0,4% 96%,100% 96%,100% 100%,0 100%)"></div>
<div class="ph" role="img" aria-label="Team of developers working at computers in an office" style="left:86px;top:2099px;width:457px;height:338px;background:linear-gradient(135deg,#d8c8a8,#7f8a94 55%,#3c4450)"></div>
<div class="abs about-h">ABOUT VANTREL WORKS</div>
<div class="abs about-p">Nemo enim ipsam voluptatem quia voluptas sit aspernatur aut odit aut fugit, sed quia consequuntur magni dolores eos qui ratione voluptatem sequi nesciunt. Neque porro quisquam est, qui dolorem ipsum quia dolor sit amet, consectetur, adipisci velit, sed quia non numquam eius modi tempora incidunt ut labore et dolore magnam aliquam quaerat voluptatem.</div>
<div class="abs btn btn-solid" style="left:571px;top:2358px;width:178px;height:42px">Read More</div>
<div class="ph" role="img" aria-label="Teal chameleon on a branch" style="left:970px;top:2330px;width:230px;height:193px;background:radial-gradient(ellipse at 55% 50%,#2f8a80 0%,#6b4a35 45%,rgba(255,255,255,0) 72%)"></div>

<!-- testimonials -->
<div class="ph" role="img" aria-label="Blue digital network background" style="left:0;top:2523px;width:1200px;height:380px;background:linear-gradient(120deg,#0a3b8f,#1060bd 50%,#0a3b8f)"></div>
<div class="abs section-h" style="top:2580px;font-size:32px;color:#fff">TESTIMONIALS</div>
<div class="abs testi-p">Vivamus scelerisque lectus aliquam elit pharetra, vel auctor risus posuere. Nam vel eros malesuada, posuere ante ac, ullamcorper nulla. Vestibulum ultrices dictum mi non iaculis. Quisque tincidunt orci vel ultrices scelerisque. Nullam eget arcu ac ex euismod rutrum. Fusce blandit luctus tortor ac congue. Suspendisse gravida dui mi. Curabitur egestas eget lacus sed fringilla.</div>
<div class="abs section-h" style="top:2775px;font-size:15px;color:#fff">-NAME HEADING</div>
<div class="abs arrow" style="left:72px;top:2690px;color:#fff">‹</div>
<div class="abs arrow" style="left:1108px;top:2690px;color:#fff">›</div>
<div class="abs avatar" role="img" aria-label="Client portrait" style="left:415px;top:2857px;width:96px;height:96px"></div>
<div class="abs avatar" role="img" aria-label="Client portrait" style="left:540px;top:2845px;width:120px;height:120px;border:5px solid #fff;box-shadow:0 0 0 4px var(--bright)"></div>
<div class="abs avatar" role="img" aria-label="Client portrait" style="left:690px;top:2857px;width:96px;height:96px"></div>

<!-- blog -->
<div class="abs section-h" style="top:3030px;font-size:32px;color:#222">BLOG POSTS</div>
<div class="abs post" style="left:75px">
  <div class="post-img" role="img" aria-label="Engineers in a server room" style="background:linear-gradient(135deg,#4a6a6a,#1e2e34)"><div class="post-date">MAY 05, 2021</div></div>
  <h4>NEMO ENIM IPSAM VOLUPTATEM QUIA VOLUPTAS</h4>
  <p>Nemo enim ipsam voluptatem quia voluptas sit aspernatur aut odit aut fugit, sed quia consequuntur magni dolores eos qui ratione voluptatem sequi</p>
</div>
<div class="abs post" style="left:436px">
  <div class="post-img" role="img" aria-label="Hand touching a glowing data protection interface" style="background:linear-gradient(135deg,#0e5c78,#0a2438)"><div class="post-date">MAY 05, 2021</div></div>
  <h4>NEMO ENIM IPSAM VOLUPTATEM QUIA VOLUPTAS</h4>
  <p>Nemo enim ipsam voluptatem quia voluptas sit aspernatur aut odit aut fugit, sed quia consequuntur magni dolores eos qui ratione voluptatem sequi</p>
</div>
<div class="abs post" style="left:796px">
  <div class="post-img" role="img" aria-label="Digital lock interface on blue background" style="background:linear-gradient(135deg,#0a2a5a,#0c6aa8 60%,#051a3a)"><div class="post-date">MAY 05, 2021</div></div>
  <h4>NEMO ENIM IPSAM VOLUPTATEM QUIA VOLUPTAS</h4>
  <p>Nemo enim ipsam voluptatem quia voluptas sit aspernatur aut odit aut fugit, sed quia consequuntur magni dolores eos qui ratione voluptatem sequi</p>
</div>

<!-- quick contact -->
<svg class="abs" style="top:3530px;left:0" width="1200" height="750" viewBox="0 0 1200 750">
  <defs><linearGradient id="contactBg" x1="0" y1="0" x2="1" y2="1"><stop offset="0" stop-color="#0b1f78"/><stop offset=".5" stop-color="#0d2f9a"/><stop offset="1" stop-color="#081858"/></linearGradient></defs>
  <path d="M0 110 C150 90 300 70 420 30 C520 0 560 90 680 95 C800 100 900 40 1000 55 C1100 70 1150 60 1200 60 L1200 750 L0 750Z" fill="url(#contactBg)" role="img" aria-label="Deep blue digital network background"/>
</svg>
<div class="abs section-h" style="top:3756px;font-size:32px;color:#fff">QUICK CONTACT</div>
<div class="abs field" style="left:163px;top:3840px;width:424px">Full Name</div>
<div class="abs field" style="left:613px;top:3840px;width:423px">Last Name</div>
<div class="abs field" style="left:163px;top:3900px;width:424px">Email *</div>
<div class="abs field" style="left:613px;top:3900px;width:423px">Company Name</div>
<div class="abs field" style="left:163px;top:3960px;width:424px">Phone Number</div>
<div class="abs field" style="left:613px;top:3960px;width:423px">Subject</div>
<div class="abs field" style="left:163px;top:4020px;width:873px;height:115px">Message</div>
<div class="abs btn" style="left:495px;top:4153px;width:210px;height:44px;background:var(--nav);font-size:18px">SUBMIT</div>

<!-- footer -->
<div class="abs" style="left:0;top:4278px;width:1200px;height:402px;background:var(--footer)"></div>
<div class="abs brand" style="top:4372px">
  <div class="brand-mark" style="width:74px;height:74px"></div>
  <div><div class="brand-name" style="color:#fff;font-size:30px">Vantrel Works</div><div class="brand-tag" style="color:#fff">CYBERSECURE YOUR BUSINESS</div></div>
</div>
<div class="abs" style="left:75px;top:4480px;display:flex;align-items:center;gap:18px;color:#fff;font-size:16px">
  <div class="foot-icon"><svg width="16" height="16" viewBox="0 0 24 24"><path fill="#fff" d="M6.6 10.8a15 15 0 006.6 6.6l2.2-2.2c.3-.3.7-.4 1-.2 1.1.4 2.3.6 3.6.6.6 0 1 .4 1 1V20c0 .6-.4 1-1 1A17 17 0 013 4c0-.6.4-1 1-1h3.5c.6 0 1 .4 1 1 0 1.3.2 2.5.6 3.6.1.3 0 .7-.2 1z"/></svg></div>1-800-555-0142
</div>
<div class="abs" style="left:75px;top:4552px;display:flex;align-items:center;gap:18px;color:#fff;font-size:16px">
  <div class="foot-icon"><svg width="16" height="12" viewBox="0 0 24 18"><rect width="24" height="18" rx="2" fill="#fff"/><path d="M1 2l11 8 11-8" stroke="#1b1b1b" stroke-width="2" fill="none"/></svg></div>info@vantrelworks.example
</div>
<div class="abs" style="left:423px;top:4353px">
  <div class="foot-h">QUICK LINKS</div>
  <ul class="foot-list"><li>Home</li><li>Who We Are</li><li>What We Do</li><li>Clients</li><li>Our Work</li><li>Blog</li><li>Contact</li></ul>
</div>
<div class="abs" style="left:641px;top:4353px">
  <div class="foot-h">SERVICES</div>
  <ul class="foot-list"><li>Neque porro quisquam</li><li>Estqui dolorem</li><li>Ipsum quia dolor</li><li>St ametcon</li><li>Sectetur</li></ul>
</div>
<div class="abs" style="left:888px;top:4353px">
  <div class="foot-h">RESOURCES</div>
  <ul class="foot-list"><li>Neque porro quisquam</li><li>Estqui dolorem</li><li>Ipsum quia dolor</li><li>St ametcon</li><li>Sectetur</li></ul>
</div>
<div class="abs social" style="left:880px;top:4585px">
  <span>Pulsa</span><span>Chirpo</span><span>Snapo</span><span>Linko</span><span>Vidra</span>
</div>
<div class="abs copy">Copyright © 2021 Company Name.&nbsp; All Right Reserved</div>

</body>
</html>
```